Powerpoint template for Trivia Company

Revamp of our current powerpoint template to make it more professional and fun for the players. Something worthy of a trivia company. Please see logo attached for potential colour - but also open to other ideas.

NO BRANDING REQUIRED (IE: No mention of our company or logo on the template please)

Target Market(s)

Bars/restaurants

Colors
3176b5
00a990

```html
<!DOCTYPE html>
<html lang="en">
<head>
<meta charset="utf-8">
<title>Trivia Night Presentation Template</title>
<link href="https://fonts.googleapis.com/css2?family=Montserrat:ital,wght@0,400;0,500;0,600;0,700;0,800;1,600&display=swap" rel="stylesheet">
<style>
:root{
  --blue:#3176b5;
  --blue-deep:#2a64a6;
  --green:#00a990;
  --green-deep:#129276;
  --ink:#2f3236;
  --paper:#eef0f2;
  --stage:#e8e9eb;
  --white:#ffffff;
  --placeholder:#d9dde2;
}
*{box-sizing:border-box;margin:0;padding:0}
html,body{width:1200px;height:2257px;overflow:hidden}
body{background:var(--stage);font-family:'Montserrat',sans-serif;color:var(--ink);position:relative}

.hero{position:absolute;left:320px;top:170px;width:373px;height:210px;transform:scale(1.5);transform-origin:0 0;box-shadow:0 10px 30px rgba(0,0,0,.15)}

.deck{position:absolute;left:23px;top:693px;display:grid;grid-template-columns:repeat(3,373px);grid-auto-rows:210px;gap:12px 18px}

.slide{position:relative;width:373px;height:210px;overflow:hidden;background:linear-gradient(135deg,#f6f7f8,var(--paper))}
.slide.framed::before,.slide.framed::after{content:"";position:absolute;width:22px;height:22px;border-radius:50%;border:3px solid var(--blue)}
.slide.framed::before{top:-11px;right:-11px}
.slide.framed::after{bottom:-11px;left:-11px}
.corner-g{position:absolute;width:22px;height:22px;border-radius:50%;border:3px solid var(--green)}
.corner-g.tl{top:-11px;left:-11px}
.corner-g.br{bottom:-11px;right:-11px}
.page-no{position:absolute;right:8px;bottom:6px;font-size:4px;color:#777}

/* welcome */
.welcome .photo{position:absolute;inset:0}
.welcome-title{position:absolute;left:17px;top:50px;color:var(--white);font-weight:800;font-size:21px;letter-spacing:.3px;line-height:1}
.welcome-title span{display:block;font-size:13px;font-weight:700;margin-top:6px}

/* cards */
.card{position:absolute;background:var(--white);box-shadow:0 2px 8px rgba(0,0,0,.08);border-radius:4px}
.rules-card{left:20px;top:14px;right:14px;bottom:20px;padding:13px 18px}
.rules-card.blue{background:linear-gradient(180deg,var(--blue-deep),var(--blue));color:var(--white)}
.card-head{font-size:9px;font-weight:800;color:var(--blue);position:relative;padding-bottom:6px}
.card-head::after{content:"";position:absolute;left:0;bottom:0;width:10px;height:1.5px;background:var(--green)}
.rules-card.blue .card-head{color:var(--white)}
.rules-list{list-style:none;margin-top:6px}
.rules-list li{font-size:5px;line-height:1.3;margin-bottom:2.4px;padding-left:5px;position:relative}
.rules-list li::before{content:"•";position:absolute;left:0;color:var(--green)}

.cat-card{left:14px;top:14px;right:14px;bottom:20px;padding:14px 18px}
.cat-grid{display:grid;grid-template-columns:1fr 1fr;grid-template-rows:repeat(5,27px);grid-auto-flow:column;margin-top:8px;column-gap:10px}
.cat{display:flex;align-items:center;gap:7px;font-size:6.2px;line-height:1.25}
.cat b{flex:none;width:13px;height:13px;border-radius:50%;color:var(--white);font-size:7px;display:flex;align-items:center;justify-content:center;background:var(--green)}
.cat.b b{background:var(--blue)}

/* section slides */
.section .shape{position:absolute;inset:0}
.section-title{position:absolute;left:19px;top:56px;font-weight:800;font-size:21px;color:var(--blue);line-height:1.08}
.section-title small{display:block;font-size:13px;color:var(--ink);font-weight:700;margin-top:4px}
.section.green .section-title{color:var(--green);top:55px}

/* question slides */
.big-letter{position:absolute;left:-14px;top:-18px;font-size:190px;font-weight:800;line-height:1;background:linear-gradient(170deg,var(--blue) 35%,#d8e4f1 95%);-webkit-background-clip:text;background-clip:text;color:transparent}
.q-green .big-letter{background-image:linear-gradient(170deg,var(--green) 35%,#d4efe9 95%)}
.q-card{left:77px;top:31px;right:0;bottom:23px;border-radius:4px 0 0 4px}
.q-pill{position:absolute;left:77px;top:42px;width:270px;height:22px;border-radius:11px;background:var(--blue);color:var(--white);font-size:10px;font-weight:700;padding:5px 14px}
.q-green .q-pill{background:linear-gradient(90deg,var(--green-deep),var(--green))}
.q-num{position:absolute;left:92px;top:71px;font-size:12px;font-weight:800;color:var(--blue)}
.q-green .q-num{color:var(--green)}
.q-num::after{content:"";position:absolute;left:0;top:20px;width:14px;height:2px;background:var(--green)}
.q-green .q-num::after{background:var(--blue)}
.q-text{position:absolute;left:92px;top:104px;width:255px;font-size:12.3px;line-height:1.25;color:#333}

/* answers */
.answer-letter{position:absolute;left:0;top:22px;font-size:118px;font-weight:800;line-height:1;color:var(--green)}
.a-card{left:77px;top:31px;right:0;bottom:23px}
.a-pill{position:absolute;left:77px;top:42px;width:80px;height:21px;border-radius:0 11px 11px 0;background:var(--green);color:var(--white);font-size:10px;font-weight:800;padding:5px 10px}
.a-list{position:absolute;left:87px;top:72px;display:grid;grid-template-columns:145px 140px;grid-template-rows:repeat(5,20.5px);grid-auto-flow:column}
.a-list li{list-style:none;font-size:8.6px;font-weight:700;color:var(--ink)}
.a-list li i{font-style:normal;color:var(--blue);margin-right:6px}

/* logo round */
.logo-board{left:14px;top:34px;right:14px;bottom:20px;padding:12px 16px;display:grid;grid-template-columns:repeat(5,1fr);gap:10px 9px}
.tile{position:relative;background:var(--white);border-radius:4px;box-shadow:0 1px 5px rgba(0,0,0,.12);display:flex;align-items:center;justify-content:center;text-align:center;font-size:6.6px;font-weight:700;color:var(--ink);padding:3px}
.tile .n{position:absolute;left:-2px;top:-3px;width:12px;height:10px;border-radius:2px;background:var(--green);color:var(--white);font-size:5.5px;display:flex;align-items:center;justify-content:center}
.tile .n.b{background:var(--blue)}
.logo-board.answers{top:34px;gap:4px 9px;grid-template-rows:repeat(2,1fr)}
.ans-cell{display:flex;flex-direction:column;gap:3px}
.ans-cell .tile{height:40px}
.ans-cell .dot{width:18px;height:18px;border-radius:50%;background:var(--placeholder)}
.ans-cell p{font-size:5px;font-weight:700;text-align:center;line-height:1.15}
.ans-tag{position:absolute;left:126px;top:34px;width:120px;height:13px;background:var(--green);color:var(--white);font-size:7px;font-weight:800;text-align:center;padding-top:2px;border-radius:0 0 6px 6px}
</style>
</head>
<body>

<!-- featured title slide -->
<section class="slide welcome hero">
  <svg class="photo" viewBox="0 0 373 210" width="373" height="210" role="img" aria-label="Photo of friends cheering at a trivia night, toned in blue">
    <defs>
      <linearGradient id="photoTone" x1="0" y1="0" x2="1" y2="1">
        <stop offset="0" stop-color="#4d6f96"/><stop offset="1" stop-color="#7b8ea3"/>
      </linearGradient>
    </defs>
    <rect width="373" height="210" fill="url(#photoTone)"/>
    <path d="M0 0H312C305 120 190 175 0 182Z" fill="#2f6fb0" opacity=".93"/>
    <path d="M373 0V210H252C318 160 360 90 373 0Z" fill="#1aa98a"/>
  </svg>
  <h1 class="welcome-title">WELCOME TO<span>TRIVIA NIGHT!</span></h1>
</section>

<main class="deck">

  <section class="slide welcome">
    <svg class="photo" viewBox="0 0 373 210" width="373" height="210" role="img" aria-label="Photo of friends cheering at a trivia night, toned in blue">
      <rect width="373" height="210" fill="url(#photoTone)"/>
      <path d="M0 0H312C305 120 190 175 0 182Z" fill="#2f6fb0" opacity=".93"/>
      <path d="M373 0V210H252C318 160 360 90 373 0Z" fill="#1aa98a"/>
    </svg>
    <h1 class="welcome-title">WELCOME TO<span>TRIVIA NIGHT!</span></h1>
  </section>

  <section class="slide framed">
    <i class="corner-g tl"></i><i class="corner-g br"></i>
    <div class="card rules-card">
      <h2 class="card-head">THE RULES</h2>
      <ul class="rules-list">
        <li>Teams may have a maximum of 6 players.</li>
        <li>No outside help (internet, phone, etc.) of any kind, including during breaks! If you are caught, your team will be disqualified.</li>
        <li>The game is comprised of 7 rounds of 10 questions–each round is worth 20 points unless otherwise noted. At the end of each round, teams will exchange answer sheets to be graded. After 7 rounds, there will be a FINAL TRIVIA round where each team may wager up to 20 points on a single question.</li>
        <li>Before the game begins, each team must pick one BONUS category (excluding the Final Trivia round) for which they will be awarded double points.</li>
        <li>In the event of a tie, a tie-breaker question will decide the winner. In the unlikely event that the tied teams each answer the question correctly (closest), the winner shall be the team which hands the correct answer to the Quizmaster the quickest.</li>
        <li>The winning team (defined as 2 or more members on the same team, or 1 member if the winner was an individual) from the previous week shall be assessed a handicap equal to ½ of their winning margin (rounded down).</li>
        <li>The Quizmaster has final say on all rule interpretations and disputes.</li>
      </ul>
    </div>
    <span class="page-no">2</span>
  </section>

  <section class="slide framed">
    <i class="corner-g tl"></i><i class="corner-g br"></i>
    <div class="card rules-card blue">
      <h2 class="card-head">THE RULES</h2>
      <ul class="rules-list">
        <li>Teams may have a maximum of 6 players.</li>
        <li>No outside help (internet, phone, etc.) of any kind, including during breaks! If you are caught, your team will be disqualified.</li>
        <li>The game is comprised of 7 rounds of 10 questions–each round is worth 20 points unless otherwise noted. At the end of each round, teams will exchange answer sheets to be graded. After 7 rounds, there will be a FINAL TRIVIA round where each team may wager up to 20 points on a single question.</li>
        <li>Before the game begins, each team must pick one BONUS category (excluding the Final Trivia round) for which they will be awarded double points.</li>
        <li>In the event of a tie, a tie-breaker question will decide the winner. In the unlikely event that the tied teams each answer the question correctly (closest), the winner shall be the team which hands the correct answer to the Quizmaster the quickest.</li>
        <li>The winning team (defined as 2 or more members on the same team, or 1 member if the winner was an individual) from the previous week shall be assessed a handicap equal to ½ of their winning margin (rounded down).</li>
        <li>The Quizmaster has final say on all rule interpretations and disputes.</li>
      </ul>
    </div>
    <span class="page-no">3</span>
  </section>

  <section class="slide framed">
    <i class="corner-g tl"></i><i class="corner-g br"></i>
    <div class="card cat-card">
      <h2 class="card-head">THIS QUIZ CONTAINS THE FOLLOWING CATEGORIES:</h2>
      <div class="cat-grid">
        <div class="cat"><b>1</b>General Knowledge</div>
        <div class="cat b"><b>2</b>One Word Movie Titles</div>
        <div class="cat"><b>3</b>Name That Year – 2001-2010 Edition<br>(Each Year is Represented)</div>
        <div class="cat b"><b>4</b>Picture Round – One Letter Logos –<br>Name the Brand/Company</div>
        <div class="cat"><b>5</b>Audio Round – Duets –<br>Name the Song and Both Artists</div>
        <div class="cat b"><b>6</b>Hey Mom, I Got an “A” in Geography!</div>
        <div class="cat"><b>7</b>Mmmmm... Beer</div>
        <div class="cat b"><b>8</b>Final Trivia Round</div>
        <div class="cat"><b>9</b>Tie Breaker Question</div>
      </div>
    </div>
    <span class="page-no">4</span>
  </section>

  <section class="slide section">
    <svg class="shape" viewBox="0 0 373 210" width="373" height="210" aria-hidden="true">
      <rect width="373" height="210" fill="#fff"/>
      <path d="M312 0H373V210H0V184C160 176 268 110 312 0Z" fill="var(--blue)"/>
    </svg>
    <h2 class="section-title">First Category:<small>General Knowledge</small></h2>
  </section>

  <section class="slide framed q-blue">
    <i class="corner-g tl"></i><i class="corner-g br"></i>
    <span class="big-letter" aria-hidden="true">Q</span>
    <div class="card q-card"></div>
    <div class="q-pill">General Knowledge</div>
    <div class="q-num">Question #1</div>
    <p class="q-text">What men’s evening wear got its name from a park in the Hudson Valley where New York’s elite were known to congregate in the 1890s?</p>
    <span class="page-no">6</span>
  </section>

  <section class="slide framed q-green">
    <i class="corner-g tl"></i><i class="corner-g br"></i>
    <span class="big-letter" aria-hidden="true">Q</span>
    <div class="card q-card"></div>
    <div class="q-pill">General Knowledge</div>
    <div class="q-num">Question #2</div>
    <p class="q-text">In the language of international warfare, what do the letters SAM mean?</p>
    <span class="page-no">7</span>
  </section>

  <section class="slide framed q-blue">
    <i class="corner-g tl"></i><i class="corner-g br"></i>
    <span class="big-letter" aria-hidden="true">Q</span>
    <div class="card q-card"></div>
    <div class="q-pill">General Knowledge</div>
    <div class="q-num">Question #3</div>
    <p class="q-text">Who is the eldest of<br>the Calloway sisters?</p>
    <span class="page-no">8</span>
  </section>

  <section class="slide framed q-green">
    <i class="corner-g tl"></i><i class="corner-g br"></i>
    <span class="big-letter" aria-hidden="true">Q</span>
    <div class="card q-card"></div>
    <div class="q-pill">General Knowledge</div>
    <div class="q-num">Question #4</div>
    <p class="q-text">The Louisiana Purchase occurred during the administration of which U.S. President?</p>
    <span class="page-no">9</span>
  </section>

  <section class="slide framed q-blue">
    <i class="corner-g tl"></i><i class="corner-g br"></i>
    <span class="big-letter" aria-hidden="true">Q</span>
    <div class="card q-card"></div>
    <div class="q-pill">General Knowledge</div>
    <div class="q-num">Question #5</div>
    <p class="q-text">Before getting their own long-running series, <em>The Pickfords</em> appeared in animated shorts on a variety show starring what British comedienne?</p>
    <span class="page-no">10</span>
  </section>

  <section class="slide framed q-green">
    <i class="corner-g tl"></i><i class="corner-g br"></i>
    <span class="big-letter" aria-hidden="true">Q</span>
    <div class="card q-card"></div>
    <div class="q-pill">General Knowledge</div>
    <div class="q-num">Question #6</div>
    <p class="q-text">What was the sub-title of<br>the second <em>Max Ventano</em> movie?</p>
    <span class="page-no">11</span>
  </section>

  <section class="slide framed q-blue">
    <i class="corner-g tl"></i><i class="corner-g br"></i>
    <span class="big-letter" aria-hidden="true">Q</span>
    <div class="card q-card"></div>
    <div class="q-pill">General Knowledge</div>
    <div class="q-num">Question #7</div>
    <p class="q-text">Who served as Prime Minister of Pakistan from 1988 to 1990 and again from 1993 to 1996?</p>
    <span class="page-no">12</span>
  </section>

  <section class="slide framed q-green">
    <i class="corner-g tl"></i><i class="corner-g br"></i>
    <span class="big-letter" aria-hidden="true">Q</span>
    <div class="card q-card"></div>
    <div class="q-pill">General Knowledge</div>
    <div class="q-num">Question #8</div>
    <p class="q-text">Which nation is the only member of NATO that does not have a standing army?</p>
    <span class="page-no">13</span>
  </section>

  <section class="slide framed q-blue">
    <i class="corner-g tl"></i><i class="corner-g br"></i>
    <span class="big-letter" aria-hidden="true">Q</span>
    <div class="card q-card"></div>
    <div class="q-pill">General Knowledge</div>
    <div class="q-num">Question #9</div>
    <p class="q-text">Which planet in our solar system is named for the messenger of the gods in Roman mythology?</p>
    <span class="page-no">14</span>
  </section>

  <section class="slide framed q-green">
    <i class="corner-g tl"></i><i class="corner-g br"></i>
    <span class="big-letter" aria-hidden="true">Q</span>
    <div class="card q-card"></div>
    <div class="q-pill">General Knowledge</div>
    <div class="q-num">Question #10</div>
    <p class="q-text">Which nation is the only member of NATO that does not have a standing army?</p>
    <span class="page-no">15</span>
  </section>

  <section class="slide section green">
    <svg class="shape" viewBox="0 0 373 210" width="373" height="210" aria-hidden="true">
      <rect width="373" height="210" fill="#fff"/>
      <path d="M286 0H373V210H0V186C150 178 262 110 286 0Z" fill="var(--green-deep)"/>
    </svg>
    <h2 class="section-title">Please Pass<br>Your Answers<small>to a neighboring team</small></h2>
  </section>

  <section class="slide framed">
    <i class="corner-g tl"></i><i class="corner-g br"></i>
    <span class="answer-letter" aria-hidden="true">A</span>
    <div class="card a-card"></div>
    <div class="a-pill">ANSWERS</div>
    <ol class="a-list">
      <li><i>1.</i>Tuxedo</li>
      <li><i>2.</i>Surface to Air Missile</li>
      <li><i>3.</i>Corinne (born in 1979)</li>
      <li><i>4.</i>Thomas Whitfield</li>
      <li><i>5.</i>Tracey Holloway</li>
      <li><i>6.</i>Back to the Jungle</li>
      <li><i>7.</i>Amara Bashir</li>
      <li><i>8.</i>The Harbor City Herons</li>
      <li><i>9.</i>Mercury</li>
      <li><i>10.</i>Iceland</li>
    </ol>
    <span class="page-no">17</span>
  </section>

  <section class="slide section">
    <svg class="shape" viewBox="0 0 373 210" width="373" height="210" aria-hidden="true">
      <rect width="373" height="210" fill="#fff"/>
      <path d="M286 0H373V210H0V186C150 178 262 110 286 0Z" fill="var(--blue)"/>
    </svg>
    <h2 class="section-title" style="top:68px">Picture Round:<small>One Letter Logos – Name<br>the Brand/Company</small></h2>
  </section>

  <section class="slide framed">
    <i class="corner-g tl"></i><i class="corner-g br"></i>
    <div class="card logo-board">
      <div class="tile"><span class="n">1</span>Dunmore</div>
      <div class="tile"><span class="n b">2</span>Quvo</div>
      <div class="tile"><span class="n">3</span>Avelo</div>
      <div class="tile"><span class="n b">4</span>Xentra</div>
      <div class="tile"><span class="n">5</span>Pinora</div>
      <div class="tile"><span class="n b">6</span>Yarrow</div>
      <div class="tile"><span class="n">7</span>Riverstone</div>
      <div class="tile"><span class="n b">8</span>Zephyr</div>
      <div class="tile"><span class="n">9</span>Nocturo</div>
      <div class="tile"><span class="n b">10</span>Wexley</div>
    </div>
    <span class="page-no">19</span>
  </section>

  <section class="slide section green">
    <svg class="shape" viewBox="0 0 373 210" width="373" height="210" aria-hidden="true">
      <rect width="373" height="210" fill="#fff"/>
      <path d="M286 0H373V210H0V186C150 178 262 110 286 0Z" fill="var(--green-deep)"/>
    </svg>
    <h2 class="section-title">Please Pass<br>Your Answers<small>to a neighboring team</small></h2>
  </section>

  <section class="slide framed">
    <i class="corner-g tl"></i><i class="corner-g br"></i>
    <div class="card logo-board answers">
      <div class="ans-cell"><div class="tile"><span class="n">1</span><i class="dot"></i></div><p>DUNMORE</p></div>
      <div class="ans-cell"><div class="tile"><span class="n b">2</span><i class="dot"></i></div><p>QUVO</p></div>
      <div class="ans-cell"><div class="tile"><span class="n">3</span><i class="dot"></i></div><p>AVELO</p></div>
      <div class="ans-cell"><div class="tile"><span class="n b">4</span><i class="dot"></i></div><p>XENTRA</p></div>
      <div class="ans-cell"><div class="tile"><span class="n">5</span><i class="dot"></i></div><p>PINORA</p></div>
      <div class="ans-cell"><div class="tile"><span class="n b">6</span><i class="dot"></i></div><p>YARROW</p></div>
      <div class="ans-cell"><div class="tile"><span class="n">7</span><i class="dot"></i></div><p>RIVERSTONE<br>GAMES</p></div>
      <div class="ans-cell"><div class="tile"><span class="n b">8</span><i class="dot"></i></div><p>ZEPHYR<br>INSURANCE GROUP</p></div>
      <div class="ans-cell"><div class="tile"><span class="n">9</span><i class="dot"></i></div><p>NOCTURO</p></div>
      <div class="ans-cell"><div class="tile"><span class="n b">10</span><i class="dot"></i></div><p>WEXLEY</p></div>
    </div>
    <div class="ans-tag">ANSWERS</div>
    <span class="page-no">21</span>
  </section>

</main>
</body>
</html>
```